Vornel Technologies business card design

We need a business card designed with our new logo. it would be great if the card could communicate it is a technology based company.

Target Market(s)

system integrators

Industry/Entity Type

technology, IOT

Contact Information for Business Card

Name, designation, Address, telephone number, email address

Requirements
Must have
• logo and company name
Nice to have
• something to do with technology

```html
<!DOCTYPE html>
<html lang="en">
<head>
<meta charset="utf-8">
<title>Vornel Technologies – Business Card</title>
<link href="https://fonts.googleapis.com/css2?family=Montserrat:wght@400;500;700&display=swap" rel="stylesheet">
<style>
  :root {
    --orange: #f7941d;
    --charcoal: #3d3d40;
    --ink: #2b2b2e;
    --paper: #ffffff;
    --backdrop: #d9d9d9;
  }
  * { margin: 0; padding: 0; box-sizing: border-box; }
  html, body {
    width: 1200px; height: 813px; overflow: hidden;
    background: var(--backdrop);
    font-family: "Montserrat", sans-serif;
  }
  .sheet {
    position: relative; width: 1200px; height: 813px;
    display: flex; align-items: center; justify-content: center; gap: 40px;
  }
  .card {
    position: relative; width: 560px; height: 320px; overflow: hidden;
    box-shadow: 0 10px 30px rgba(0,0,0,.25);
  }
  .card-front { background: var(--paper); }
  .card-back { background: var(--charcoal); display: flex; align-items: center; justify-content: center; }
  .wave { position: absolute; inset: 0; width: 560px; height: 320px; }
  .wave-fill { fill: var(--charcoal); }
  .wave-accent { fill: none; stroke: var(--orange); stroke-width: 4; stroke-linecap: round; }

  .brand { display: flex; align-items: center; gap: 10px; }
  .brand-mark { width: 16px; height: 16px; background: var(--orange); flex: none; }
  .brand-name {
    font-weight: 700; text-transform: uppercase; line-height: 1.05; letter-spacing: 1px;
  }
  .card-front .brand { position: absolute; left: 34px; top: 128px; }
  .card-front .brand-name { color: var(--ink); font-size: 22px; }
  .card-back .brand { gap: 18px; }
  .card-back .brand-mark { width: 30px; height: 30px; }
  .card-back .brand-name { color: var(--paper); font-size: 44px; letter-spacing: 2px; }
  .brand-name small { display: block; font-size: .5em; letter-spacing: 4px; }

  .divider { position: absolute; left: 250px; top: 40px; width: 2px; height: 150px; background: var(--orange); }

  .contact { position: absolute; left: 268px; top: 38px; color: var(--ink); font-size: 11.5px; line-height: 1.4; }
  .contact-name { color: var(--orange); font-weight: 700; font-size: 15px; letter-spacing: .5px; text-transform: uppercase; }
  .contact-role { margin-bottom: 10px; }
  .contact-address { margin-bottom: 10px; }
  .contact-line { display: flex; align-items: center; gap: 7px; margin-bottom: 2px; }
  .contact-icon { width: 12px; height: 12px; fill: var(--orange); flex: none; }
</style>
</head>
<body>
<main class="sheet">
  <section class="card card-front" aria-label="Card front">
    <svg class="wave" viewBox="0 0 560 320" aria-hidden="true">
      <path class="wave-fill" d="M130 320 C330 300 430 240 500 150 C530 110 545 90 560 70 L560 320 Z"/>
      <path class="wave-accent" d="M200 300 C360 270 440 200 490 130 C515 95 530 70 545 52"/>
    </svg>

    <div class="brand">
      <span class="brand-mark"></span>
      <span class="brand-name">Vornel<small>Technologies</small></span>
    </div>

    <div class="divider"></div>

    <div class="contact">
      <p class="contact-name">Dalen Fairbrook</p>
      <p class="contact-role">Owner/Co-Founder</p>
      <p class="contact-address">Northgate Plaza 2100 Elm<br>Riverside WD Suite 310</p>
      <p class="contact-line">
        <svg class="contact-icon" viewBox="0 0 24 24" aria-hidden="true"><path d="M6.6 10.8a15 15 0 0 0 6.6 6.6l2.2-2.2a1 1 0 0 1 1-.25 11.4 11.4 0 0 0 3.6.57 1 1 0 0 1 1 1V20a1 1 0 0 1-1 1A17 17 0 0 1 3 4a1 1 0 0 1 1-1h3.5a1 1 0 0 1 1 1c0 1.25.2 2.45.57 3.57a1 1 0 0 1-.25 1z"/></svg>
        555-014-2293
      </p>
      <p class="contact-line">
        <svg class="contact-icon" viewBox="0 0 24 24" aria-hidden="true"><path d="M2 5h20v14H2z M2 5l10 8 10-8" /></svg>
        info@vorneltech.com
      </p>
      <p class="contact-line">
        <svg class="contact-icon" viewBox="0 0 24 24" aria-hidden="true"><circle cx="12" cy="12" r="10"/></svg>
        www.vorneltech.com
      </p>
    </div>
  </section>

  <section class="card card-back" aria-label="Card back">
    <div class="brand">
      <span class="brand-mark"></span>
      <span class="brand-name">Vornel<small>Technologies</small></span>
    </div>
  </section>
</main>
</body>
</html>
```